Roofing Company Realtor Marketing Flyer

We would like a design for marketing material aimed at realtors. We are seeking to build relationships with local realtors to ensure that both sellers and buyers are happy and confident with their roofing systems through roof inspections, No-Leak certification, roof repairs, and replacements if necessary.

There are three points that must be included:
1. Home inspectors are generalists. We are roof experts that specialize in diagnosing and fixing roofing problems.
2. We offer "No Leak" certification to offer peace of mind to homeowners.
3. We offer referral bonuses for realtors.

Target Market(s)

Realtors

Industry/Entity Type

Roofing

Font styles to use
Sans Serif

Colors

Designer to choose colors to be used in the design.

Requirements
Must have
• Must be double-sided.
• Must be similar to current marketing materials design. See website http://shinglecrestpro.com and attached images for details.
• We would also like a "fanned out" version of our Sample Inspection Report showing glimpses of some of the images on the later pages (See attached documents).

```html
<!DOCTYPE html>
<html lang="en">
<head>
<meta charset="utf-8">
<title>ShingleCrest Pro – Realtor Flyer</title>
<link href="https://fonts.googleapis.com/css2?family=Lato:wght@400;700;900&display=swap" rel="stylesheet">
<style>
  :root{
    --orange:#f28a1f;
    --orange-deep:#e0701a;
    --grey-dark:#55575a;
    --grey-text:#3c3d40;
    --white:#ffffff;
    --stage:#1d1f23;
  }
  *{box-sizing:border-box;margin:0;padding:0}
  html,body{width:1200px;height:848px;overflow:hidden}
  body{background:var(--stage);font-family:'Lato',sans-serif;position:relative}
  .flyer{position:absolute;left:317px;top:24px;width:566px;height:800px;background:var(--white);overflow:hidden;box-shadow:0 10px 30px rgba(0,0,0,.5)}
  .flyer-shapes{position:absolute;inset:0}
  .brand{position:absolute;left:40px;top:44px;display:flex;align-items:center;gap:10px}
  .brand-mark{width:14px;height:14px;background:var(--orange)}
  .brand-name{font-weight:700;font-size:38px;color:var(--orange);letter-spacing:.5px}
  .phone{position:absolute;right:22px;top:146px;color:var(--white);font-weight:900;font-size:22px;letter-spacing:1px}
  .points{position:absolute;inset:0}
  .point{position:absolute;text-align:center;color:var(--grey-text);font-size:15px;line-height:1.3}
  .point svg{display:block;margin:0 auto 8px}
  .point-experts{left:30px;top:492px;width:200px}
  .point-noleak{left:200px;top:600px;width:180px}
  .point-referral{left:388px;top:616px;width:160px}
  .badges{position:absolute;left:196px;top:704px;display:flex;gap:10px;align-items:center}
  .badge{width:28px;height:28px;border-radius:50%}
  .badge.green{background:#4f9a3a}
  .badge.blue{background:#3a6fb5}
  .badge.red{background:#c23a3a}
  .badge.grey{background:#9a9a9a}
  .badge.navy{background:#2b3553}
  .website{position:absolute;left:34px;bottom:24px;color:var(--white);font-size:24px;letter-spacing:.5px}
</style>
</head>
<body>
  <article class="flyer">
    <svg class="flyer-shapes" width="566" height="800" viewBox="0 0 566 800">
      <defs>
        <linearGradient id="roofPhoto" x1="0" y1="0" x2="1" y2="0.4">
          <stop offset="0" stop-color="#5a3418"/>
          <stop offset="0.45" stop-color="#c0621c"/>
          <stop offset="0.75" stop-color="#a0483a"/>
          <stop offset="1" stop-color="#9a8a86"/>
        </linearGradient>
      </defs>
      <polygon points="0,128 566,112 566,128 0,144" fill="var(--orange)"/>
      <g role="img" aria-label="Photo of a roofer walking across worn shingles">
        <polygon points="0,144 566,128 566,440 0,470" fill="url(#roofPhoto)"/>
      </g>
      <polygon points="330,132 566,126 566,182 355,182" fill="var(--orange)"/>
      <polygon points="0,462 566,432 566,448 0,480" fill="var(--grey-dark)"/>
      <polygon points="252,540 566,588 566,596 248,547" fill="var(--orange)"/>
      <polygon points="0,742 330,742 360,800 0,800" fill="var(--orange)"/>
      <polygon points="330,742 566,722 566,800 360,800" fill="var(--grey-dark)"/>
    </svg>

    <div class="brand">
      <span class="brand-mark"></span>
      <span class="brand-name">ShingleCrest Pro</span>
    </div>
    <div class="phone">877-555-0142</div>

    <div class="points">
      <div class="point point-experts">
        <svg width="54" height="40" viewBox="0 0 54 40"><ellipse cx="27" cy="20" rx="24" ry="17" fill="none" stroke="var(--orange)" stroke-width="3"/><path d="M16 20 L25 29 L48 6" fill="none" stroke="var(--orange)" stroke-width="4" stroke-linecap="round"/></svg>
        Home inspectors are generalists. We are roof experts that specialize in diagnosing and fixing roofing problems.
      </div>
      <div class="point point-noleak">
        <svg width="54" height="40" viewBox="0 0 54 40"><ellipse cx="27" cy="20" rx="24" ry="17" fill="none" stroke="var(--orange)" stroke-width="3"/><path d="M16 20 L25 29 L48 6" fill="none" stroke="var(--orange)" stroke-width="4" stroke-linecap="round"/></svg>
        We offer "No Leak" certification to offer peace of mind to homeowners.
      </div>
      <div class="point point-referral">
        <svg width="54" height="40" viewBox="0 0 54 40"><ellipse cx="27" cy="20" rx="24" ry="17" fill="none" stroke="var(--orange)" stroke-width="3"/><path d="M16 20 L25 29 L48 6" fill="none" stroke="var(--orange)" stroke-width="4" stroke-linecap="round"/></svg>
        We offer referral bonuses for realtors.
      </div>
    </div>

    <div class="badges" aria-label="Certifications">
      <span class="badge green"></span>
      <span class="badge blue"></span>
      <span class="badge red"></span>
      <span class="badge grey"></span>
      <span class="badge navy"></span>
    </div>

    <div class="website">www.ShingleCrestPro.com</div>
  </article>
</body>
</html>
```